New design for our thank you cards *

We need Thank You card designs for our mortgage broking company "Harrowgate Lending". We have an existing design and need a revamp of these. We are a boutique broking firm and would like "thank you" cards to send to our clients who refer new clients.

We are a referral-based business, our success and longevity is inextricably linked to the advice and service we provide our clients and referral partners.

Industry/Entity Type

Mortgage Brokerage

Colors
0792cd
0255a3
3176b5
33a6d7
85acd3
85cae6
cee9f5
cedeed
ffffff

Requirements
Must have
• our logo on the front 7 thank you & print on the back

```html
<!DOCTYPE html>
<html lang="en">
<head>
<meta charset="utf-8">
<title>Harrowgate Lending – Thank You Card</title>
<link rel="stylesheet" href="https://fonts.googleapis.com/css2?family=Caveat:wght@500&family=Oswald:wght@600&display=swap">
<style>
  :root {
    --frame-blue: #0255a3;
    --paper: #ffffff;
    --rule-blue: #3a5aa8;
    --script-blue: #33a6d7;
    --heading-navy: #2b4a9c;
    --bird-deep: #1a66e0;
    --bird-mid: #3176b5;
    --bird-light: #cedeed;
  }
  html, body {
    margin: 0;
    padding: 0;
    width: 1200px;
    height: 848px;
    overflow: hidden;
    background: var(--frame-blue);
  }
  .card {
    position: relative;
    width: 1200px;
    height: 848px;
    overflow: hidden;
    background: var(--frame-blue);
  }
  .card__paper {
    position: absolute;
    left: 70px;
    top: 46px;
    width: 1058px;
    height: 748px;
    background: var(--paper);
  }
  .card__rule {
    position: absolute;
    left: 106px;
    top: 71px;
    width: 986px;
    height: 696px;
    border: 1px solid var(--rule-blue);
  }
  .card__bird {
    position: absolute;
    left: 172px;
    top: 135px;
    width: 305px;
    height: 270px;
    border-radius: 60% 40% 45% 55% / 45% 35% 65% 55%;
    background:
      radial-gradient(ellipse at 70% 30%, var(--bird-deep) 0%, var(--bird-mid) 40%, rgba(206, 222, 237, 0.9) 75%, rgba(255, 255, 255, 0) 100%);
  }
  .card__thanks {
    position: absolute;
    left: 328px;
    top: 232px;
    width: 680px;
    margin: 0;
    font-family: "Caveat", cursive;
    font-weight: 500;
    font-size: 185px;
    line-height: 1;
    color: var(--script-blue);
    word-spacing: 50px;
    white-space: nowrap;
    transform: scaleY(1.45);
    transform-origin: top left;
  }
  .card__subline {
    position: absolute;
    left: 383px;
    top: 490px;
    margin: 0;
    font-family: "Oswald", sans-serif;
    font-weight: 600;
    font-size: 60px;
    line-height: 1.2;
    color: var(--heading-navy);
    white-space: nowrap;
  }
</style>
</head>
<body>
  <main class="card">
    <div class="card__paper"></div>
    <div class="card__rule"></div>
    <div class="card__bird" role="img" aria-label="Low-poly illustration of a blue bird perched on the lettering"></div>
    <h1 class="card__thanks">Thank You</h1>
    <p class="card__subline">For Your Business</p>
  </main>
</body>
</html>
```